Mobile Tutoring Service needs a Flier for Distribution to Clients

Lantern Scholars Inc. is a tutoring company that uses video call technology to perform tutoring session in math, sciences, and standardized test preparation. We need a flier that we can distribute to email lists of parents in school districts around the St. Louis Area, as well as post in public areas to attract clients. The following file has the important information needed on the flier. In particular, the "How it Works" Steps 1-3 can be made into an animation or video that looks attractive and helps potential clients understand our process. Our logo is also found in the document. Ideally, all information in the power point slide will be in the flier.

Target Market(s)

Parents for middle and high schoolers grade 6-12 in the St. Louis Area

Industry/Entity Type

Tutoring

Font styles to use
Serif

Colors
3176b5
85abd2
0492cd
33a6d7
ceeaf5

Requirements
Must have
• All the information with the attached file
Nice to have
• A nice-looking animation instead of the still screen shoots that are included in the attached file.

```html
<!DOCTYPE html>
<html lang="en">
<head>
<meta charset="utf-8">
<title>Lantern Scholars – Mobile Tutoring Flier</title>
<link href="https://fonts.googleapis.com/css2?family=Catamaran:wght@500;700;800&family=Lato:wght@400;700&family=Oswald:wght@400;500&display=swap" rel="stylesheet">
<style>
  :root{
    --blue-deep:#3176b5;
    --blue-soft:#85abd2;
    --blue-bright:#0492cd;
    --blue-sky:#33a6d7;
    --blue-mist:#ceeaf5;
    --blue-head:#4a86c5;
    --ink:#1d1d1f;
    --red:#e3120b;
    --paper:#ffffff;
    --stage:#dcd8d2;
  }
  *{box-sizing:border-box;margin:0;padding:0}
  html,body{width:1200px;height:1200px;overflow:hidden;background:var(--stage)}
  .flier{
    position:absolute;left:152px;top:20px;width:978px;height:1266px;
    transform:scale(0.916);transform-origin:0 0;
    background:var(--paper);overflow:hidden;
    font-family:"Lato",sans-serif;color:var(--ink);
  }
  .abs{position:absolute}
  .hero-art{left:0;top:0;width:978px;height:460px}
  .brand{left:255px;top:52px;display:flex;align-items:center;gap:18px}
  .brand-mark{width:52px;height:52px;border-radius:50%;background:var(--blue-head)}
  .brand-name{font-family:"Catamaran",sans-serif;font-weight:800;font-size:54px;color:var(--ink);line-height:1}
  .device{left:55px;top:160px;width:212px;height:446px;border-radius:34px;background:#1b1b1b}
  .device-screen{position:absolute;left:16px;top:57px;width:180px;height:326px;background:linear-gradient(#ffffff,#eef2f6)}
  .device-speaker{position:absolute;left:86px;top:34px;width:40px;height:6px;border-radius:3px;background:#3a3a3a}
  .device-button{position:absolute;left:86px;top:392px;width:40px;height:40px;border-radius:50%;background:#0d0d0d;border:2px solid #333}
  .headline{right:48px;top:408px;text-align:right;font-family:"Catamaran",sans-serif;line-height:1}
  .headline .h1{font-size:72px;font-weight:800;color:var(--blue-head)}
  .headline .h2{font-size:40px;font-weight:700;color:var(--ink);margin-top:10px}
  .headline .h3{font-size:55px;font-weight:500;color:var(--blue-head);margin-top:12px}
  .facts{left:35px;top:655px;width:438px;list-style:none}
  .facts li{position:relative;padding-left:16px;font-size:15.2px;line-height:1.22;text-align:justify;margin-bottom:21px}
  .facts li::before,.plans li::before{content:"";position:absolute;left:0;top:6px;width:6px;height:6px;border-radius:50%;background:var(--blue-deep)}
  .facts .label{color:var(--blue-deep)}
  .divider{left:488px;top:618px;width:1px;height:205px;background:#d7dde4}
  .plans-title{left:506px;top:642px;font-family:"Oswald",sans-serif;font-weight:500;font-size:29px;color:var(--blue-deep);letter-spacing:-.3px}
  .plans{left:506px;top:695px;width:440px;list-style:none}
  .plans li{position:relative;padding-left:18px;font-size:21px;line-height:1.3;margin-bottom:22px}
  .plans li::before{top:9px}
  .plans b{font-weight:700}
  .plans .accent{color:var(--red);font-weight:700}
  .steps{left:35px;top:845px;width:910px;height:60px}
  .step-text{top:853px;color:#fff;font-family:"Oswald",sans-serif;font-weight:400;line-height:1.3}
  .step-1{left:46px;font-family:"Lato",sans-serif;font-size:15px}
  .step-1 b{font-weight:700}
  .step-2{left:389px;top:858px;font-size:13px}
  .step-3{left:677px;top:848px;font-size:13px}
  .shot{top:918px;height:186px;width:295px;border:2px solid var(--blue-sky);background:#fff;overflow:hidden}
  .shot-1{left:35px}
  .shot-2{left:341px;background:#e3f1f8}
  .shot-3{left:648px;background:#d7edf7}
  .avatar{position:absolute;width:22px;height:22px;border-radius:50%;background:#8a8480}
  .meta{position:absolute;font-size:8px;color:#9aa3ab}
  .photo{position:absolute}
  .chat-date{top:22px;left:0;width:100%;text-align:center;font-size:8px}
  .chat-name{font-size:8px;color:#9aa3ab}
  .chat-msg{position:absolute;left:36px;font-size:10.5px;line-height:1.35;color:#333}
  .chat-msg .num{color:var(--blue-sky)}
  .cta{left:0;top:1124px;width:978px;text-align:center;font-size:21px;color:var(--blue-deep);font-weight:700;letter-spacing:.1px}
  .footer-art{left:0;top:1175px;width:978px;height:91px}
  .contact{top:1222px;color:#fff;font-size:15.5px;display:flex;align-items:center;gap:9px}
  .contact svg{width:20px;height:20px}
  .c-web{left:35px}.c-phone{left:422px}.c-mail{right:34px}
</style>
</head>
<body>
<main class="flier">

  <svg class="abs hero-art" viewBox="0 0 978 460" role="img" aria-label="Chalkboard-style background of handwritten physics and calculus equations">
    <defs>
      <linearGradient id="boardTone" x1="0" y1="0" x2="1" y2="1">
        <stop offset="0" stop-color="#fbfbfb"/>
        <stop offset="1" stop-color="#ececec"/>
      </linearGradient>
      <linearGradient id="lowerTone" x1="0" y1="0" x2="0" y2="1">
        <stop offset="0" stop-color="#f0f1f3"/>
        <stop offset="1" stop-color="#ffffff"/>
      </linearGradient>
    </defs>
    <rect width="978" height="460" fill="url(#lowerTone)"/>
    <polygon points="0,0 978,0 978,255 360,450 0,335" fill="url(#boardTone)"/>
    <polyline points="0,335 360,450 978,255" fill="none" stroke="var(--blue-head)" stroke-width="6"/>
  </svg>

  <div class="abs brand">
    <span class="brand-mark"></span>
    <span class="brand-name">Lantern Scholars</span>
  </div>

  <div class="abs device">
    <span class="device-speaker"></span>
    <div class="device-screen" role="img" aria-label="Phone screen showing a hand-drawn right triangle problem with a=3, b=4, c=?"></div>
    <span class="device-button"></span>
  </div>

  <div class="abs headline">
    <div class="h1">Personalized</div>
    <div class="h2">tutoring from STEM experts</div>
    <div class="h3">via your mobile device</div>
  </div>

  <ul class="abs facts">
    <li><span class="label">SUBJECTS:</span> All Math, Science, Standardized Test Prep, and Writing 6th-12th grade.</li>
    <li>Our tutors are local St. Louis PhD candidates or PhD degree holders in STEM fields.</li>
    <li>No scheduling required! As soon as you send a message for help, a tutor will respond to set up a study session as soon as possible.</li>
  </ul>

  <div class="abs divider"></div>

  <h2 class="abs plans-title">PAYMENT PLANS:</h2>
  <ul class="abs plans">
    <li>Pay-as-you-go: <b>$0.83/minute</b>.<br><span class="accent">$0 up- front</span> before session begins!</li>
    <li>Unlimited Subscription: <span class="accent">$150 per month</span></li>
  </ul>

  <svg class="abs steps" viewBox="0 0 910 60" aria-hidden="true">
    <polygon points="0,0 297,0 315,30 297,60 0,60" fill="var(--blue-deep)"/>
    <polygon points="305,0 605,0 623,30 605,60 305,60 323,30" fill="#1b8fcf" stroke="#fff" stroke-width="4"/>
    <polygon points="614,0 892,0 910,30 892,60 614,60 632,30" fill="var(--blue-sky)" stroke="#fff" stroke-width="4"/>
  </svg>
  <div class="abs step-text step-1"><b>STEP 1:</b><br>Send Tutors Your Problem</div>
  <div class="abs step-text step-2">STEP 2<br>Tutor Sends Response to set up session</div>
  <div class="abs step-text step-3">STEP 3:<br>Perform Tutoring Session and<br>Receive Copy of your notes!</div>

  <section class="abs shot shot-1">
    <span class="avatar" style="left:8px;top:4px"></span>
    <span class="meta" style="left:38px;top:6px">Jordan Ellery</span>
    <div class="photo" style="left:41px;top:20px;width:210px;height:156px;background:linear-gradient(#e4e1dc,#cfcac3)" role="img" aria-label="Photo of a worksheet: find all roots of a polynomial"></div>
  </section>

  <section class="abs shot shot-2">
    <span class="meta chat-date">Dec 20, 2016, 5:09 PM</span>
    <span class="avatar" style="left:4px;top:44px"></span>
    <div class="chat-msg" style="top:46px"><span class="chat-name">Miles Harper</span><br>Hey Jordan, I will be ready to ClassCall in two<br>minutes. my phone number is <span class="num">8475550192</span><br>to give me a call!</div>
    <span class="avatar" style="left:4px;top:116px"></span>
    <div class="chat-msg" style="top:118px"><span class="chat-name">Miles Harper</span><br>Ready!</div>
  </section>

  <section class="abs shot shot-3">
    <span class="avatar" style="left:72px;top:2px;width:14px;height:14px"></span>
    <div class="photo" style="left:90px;top:12px;width:120px;height:160px;background:linear-gradient(#c8c3bc,#a9a39b)" role="img" aria-label="Photo of handwritten whiteboard notes from the session"></div>
  </section>

  <p class="abs cta">Contact us today to set up for your first, FREE tutoring session</p>

  <svg class="abs footer-art" viewBox="0 0 978 91" aria-hidden="true">
    <polygon points="0,6 490,0 978,6 978,91 0,91" fill="var(--blue-sky)"/>
    <polygon points="0,38 490,0 978,38 978,91 0,91" fill="var(--blue-deep)"/>
  </svg>

  <div class="abs contact c-web">
    <svg viewBox="0 0 20 20" aria-hidden="true"><circle cx="10" cy="10" r="8.5" fill="none" stroke="#fff" stroke-width="1.8"/><ellipse cx="10" cy="10" rx="3.5" ry="8.5" fill="none" stroke="#fff" stroke-width="1.4"/><line x1="1.5" y1="10" x2="18.5" y2="10" stroke="#fff" stroke-width="1.4"/></svg>
    <span>lanternscholars.com</span>
  </div>
  <div class="abs contact c-phone">
    <svg viewBox="0 0 20 20" aria-hidden="true"><rect x="2" y="3" width="5" height="14" rx="1" fill="none" stroke="#fff" stroke-width="1.6"/><rect x="8" y="3" width="10" height="14" rx="1" fill="none" stroke="#fff" stroke-width="1.6"/><path d="M10 6h6M10 9h2M13 9h1M15 9h1M10 12h2M13 12h1M15 12h1" stroke="#fff" stroke-width="1.4"/></svg>
    <span>866-555-0148</span>
  </div>
  <div class="abs contact c-mail">
    <svg viewBox="0 0 20 20" aria-hidden="true"><rect x="1.5" y="4" width="17" height="12" fill="none" stroke="#fff" stroke-width="1.6"/><polyline points="1.5,4 10,11 18.5,4" fill="none" stroke="#fff" stroke-width="1.6"/></svg>
    <span>tutor@lanternscholars.com</span>
  </div>

</main>
</body>
</html>
```